Dentistry

Dentist's personal business card. No logo needed. The card shoul deliver the massage of reliability, professionalism, experience.
Please ad the full brief of the project: down the line it says: the winning look should be precise and pristine NO pictures of Teeth, smiles, instruments etc.

The details to be desplaid are:
Dr. Rob Valdoni
Doctor of Dental Surgery
PHD
Web. Www.drvaldoni.com
Email. Rob@drvaldoni.com
Tel 07731482590
Surgery address. 27Bharwick road London SW4 7QN UK
82 Fenwyn Row London SW3 2HT. Uk

Reason: Decided to make the payment unrefundable in order to get more designers involved.

Requirements
Should not have
• Logo, teeth, smile any sort of instruments.

```html
<!DOCTYPE html>
<html lang="en">
<head>
<meta charset="utf-8">
<title>Dr. Rob Valdoni – Business Card</title>
<link rel="stylesheet" href="https://fonts.googleapis.com/css2?family=PT+Serif:wght@700&family=Roboto+Condensed:wght@700&display=swap">
<style>
  :root {
    --ink: #0a0a0a;
    --surgery-green: #0d6a3c;
    --paper: #ffffff;
    --backdrop: #e6e2dc;
    --shadow: rgba(0, 0, 0, 0.18);
  }
  * { margin: 0; padding: 0; box-sizing: border-box; }
  html, body {
    width: 1200px;
    height: 1200px;
    overflow: hidden;
    background: var(--backdrop);
  }
  .canvas {
    position: relative;
    width: 1200px;
    height: 1200px;
  }
  .card {
    position: absolute;
    left: 150px;
    width: 900px;
    height: 514px;
    border-radius: 40px;
    background: var(--paper);
    box-shadow: 0 10px 30px var(--shadow);
    overflow: hidden;
  }
  .card--front { top: 50px; }
  .card--back  { top: 636px; }

  .front-identity {
    position: absolute;
    inset: 0;
    display: flex;
    flex-direction: column;
    align-items: center;
    justify-content: center;
    font-family: "PT Serif", Georgia, serif;
    font-weight: 700;
    text-align: center;
  }
  .front-identity .name {
    color: var(--ink);
    font-size: 84px;
    line-height: 1;
    transform: scaleX(0.88);
    letter-spacing: -1px;
  }
  .front-identity .title {
    color: var(--surgery-green);
    font-size: 44px;
    line-height: 1.1;
    margin-top: 14px;
    transform: scaleX(0.82);
  }
  .front-identity .degree {
    color: var(--surgery-green);
    font-size: 70px;
    line-height: 1;
    margin-top: 4px;
    letter-spacing: 2px;
  }

  .back-panel {
    position: absolute;
    inset: 0;
    width: 900px;
    height: 514px;
  }
  .back-panel .panel-dark { fill: var(--ink); }
  .back-panel .panel-stripe { fill: var(--surgery-green); }

  .back-identity {
    position: absolute;
    left: 0;
    top: 150px;
    width: 360px;
    text-align: center;
    font-family: "PT Serif", Georgia, serif;
    font-weight: 700;
  }
  .back-identity .name {
    color: var(--surgery-green);
    font-size: 44px;
    line-height: 1;
    transform: scaleX(0.86);
    white-space: nowrap;
  }
  .back-identity .title {
    color: var(--paper);
    font-size: 27px;
    margin-top: 12px;
    transform: scaleX(0.8);
    white-space: nowrap;
  }
  .back-identity .degree {
    color: var(--paper);
    font-size: 58px;
    line-height: 1;
    margin-top: 10px;
    letter-spacing: 2px;
  }

  .contact-list {
    position: absolute;
    left: 432px;
    top: 110px;
    list-style: none;
    font-family: "PT Serif", Georgia, serif;
    font-weight: 700;
    color: var(--ink);
    font-size: 31px;
    line-height: 1.32;
    white-space: nowrap;
  }
  .contact-list .tel {
    font-size: 34px;
    letter-spacing: 1.5px;
  }

  .address-block {
    position: absolute;
    left: 352px;
    top: 404px;
    font-family: "Roboto Condensed", "Arial Narrow", sans-serif;
    font-style: normal;
    font-weight: 700;
    color: var(--surgery-green);
    font-size: 22px;
    line-height: 1.6;
    white-space: nowrap;
  }
  .address-block .second {
    font-size: 25px;
    letter-spacing: 0.3px;
  }
</style>
</head>
<body>
<main class="canvas">

  <section class="card card--front" aria-label="Business card front">
    <div class="front-identity">
      <h1 class="name">Dr. Rob Valdoni</h1>
      <p class="title">Doctor of Dental Surgery</p>
      <p class="degree">PHD</p>
    </div>
  </section>

  <section class="card card--back" aria-label="Business card back">
    <svg class="back-panel" viewBox="0 0 900 514" aria-hidden="true">
      <polygon class="panel-dark" points="0,0 412,0 298,514 0,514"/>
      <polygon class="panel-stripe" points="412,0 426,0 312,514 298,514"/>
    </svg>

    <div class="back-identity">
      <p class="name">Dr. Rob Valdoni</p>
      <p class="title">Doctor of Dental Surgery</p>
      <p class="degree">PHD</p>
    </div>

    <ul class="contact-list">
      <li class="web">Web: www.drvaldoni.com</li>
      <li class="email">Email: Rob@drvaldoni.com</li>
      <li class="tel">Tel 07731482590</li>
    </ul>

    <address class="address-block">
      <p class="first">Surgery address. 27Bharwick road London SW4 7QN UK</p>
      <p class="second">82 Fenwyn Row London SW3 2HT. Uk</p>
    </address>
  </section>

</main>
</body>
</html>
```